Paws Home

Need Yard signs
Dimensions 24" wide and 18" high

Copy: Rescue does not mean "Damaged". It means they have been let down by humans.
Please adopt at: 217 W Brannock Ave, Tampa, Fl 33682
Open: Tues-Sun 10am - 7pm

I have attached a sample of the original ad. I can't use this because the resolution is too low and the type has to be big enough so that it can be seen 12 feet away.
I have also attached some photos you can use. The res may not be hi enough, but perhaps you can find some stock photography even these pics are not hi res enough.

Target Market(s)

animal lovers

Font styles to use
Sans Serif

Colors

Designer to choose colors to be used in the design.

Requirements
Must have
• Must be easy to read.

```html
<!DOCTYPE html>
<html lang="en">
<head>
<meta charset="utf-8">
<title>Paws Home – Yard Sign</title>
<link href="https://fonts.googleapis.com/css2?family=Black+Ops+One&family=Alfa+Slab+One&family=Roboto+Condensed:wght@700&display=swap" rel="stylesheet">
<style>
  :root {
    --navy: #1e2a57;
    --navy-deep: #17204a;
    --navy-frame: #1d2b5e;
    --white: #f4f2ee;
    --orange: #ee6444;
    --frame-cream: #f1ede6;
    --tan: #b98a55;
    --tan-light: #c79c66;
    --wall: #9fb6ad;
  }
  * { margin: 0; padding: 0; box-sizing: border-box; }
  html, body { width: 1200px; height: 900px; overflow: hidden; }
  body { background: var(--navy); }

  .sign {
    position: relative;
    width: 1200px;
    height: 900px;
    overflow: hidden;
    background: radial-gradient(ellipse at 60% 40%, #243266 0%, var(--navy) 55%, var(--navy-deep) 100%);
    color: var(--white);
  }

  .photo-mat {
    position: absolute;
    left: 96px; top: 56px;
    width: 512px; height: 744px;
    background: var(--frame-cream);
  }
  .photo {
    position: absolute;
    left: 112px; top: 72px;
    width: 480px; height: 712px;
    background: linear-gradient(170deg, var(--wall) 0%, var(--tan-light) 30%, var(--tan) 65%, #d8cfc4 100%);
  }
  .photo-frame {
    position: absolute;
    left: 96px; top: 56px;
    width: 512px; height: 744px;
  }

  .slogan-line {
    position: absolute;
    left: 640px;
    width: 536px;
    text-align: center;
    font-family: "Black Ops One", sans-serif;
    line-height: 1;
    white-space: nowrap;
    color: var(--white);
  }
  .accent { color: var(--orange); }
  .line-1 { top: 104px; font-size: 56px; }
  .line-2 { top: 192px; font-size: 50px; }
  .line-3 { top: 270px; font-size: 66px; }
  .line-4 { top: 360px; font-size: 56px; }
  .line-5 { top: 442px; font-size: 60px; }
  .line-6 { top: 522px; font-size: 74px; }
  .line-7 { top: 618px; font-size: 70px; }

  .address {
    position: absolute;
    left: 656px; top: 722px;
    width: 480px; height: 90px;
  }
  .paw-icon { position: absolute; left: 0; top: 2px; width: 72px; height: 66px; }
  .address-text {
    position: absolute;
    font-family: "Roboto Condensed", sans-serif;
    font-weight: 700;
    font-size: 31px;
    letter-spacing: 1px;
    line-height: 1;
    white-space: nowrap;
  }
  .address-street { left: 84px; top: 18px; }
  .address-city { right: 24px; top: 60px; }

  .hours {
    position: absolute;
    left: 96px; top: 808px;
    width: 544px;
    text-align: center;
    font-family: "Alfa Slab One", sans-serif;
    font-size: 36px;
    line-height: 46px;
    letter-spacing: 1px;
  }
</style>
</head>
<body>
<main class="sign">
  <div class="photo-mat"></div>
  <div class="photo" role="img" aria-label="Photo of a tan rescue dog with a white chest sitting in a shelter kennel"></div>
  <svg class="photo-frame" viewBox="0 0 512 744" aria-hidden="true">
    <rect x="36" y="44" width="440" height="660" fill="none" stroke="var(--navy-frame)" stroke-width="12"/>
    <rect x="58" y="68" width="396" height="612" fill="none" stroke="var(--navy-frame)" stroke-width="5"/>
  </svg>

  <h1 class="slogan">
    <span class="slogan-line line-1">RESCUE DOES NOT</span>
    <span class="slogan-line line-2">MEAN <span class="accent">"DAMAGED</span></span>
    <span class="slogan-line line-3">IT MEANS</span>
    <span class="slogan-line line-4">THEY HAVE</span>
    <span class="slogan-line line-5">BEEN LET</span>
    <span class="slogan-line line-6">DOWN BY</span>
    <span class="slogan-line line-7 accent">HUMANS</span>
  </h1>

  <address class="address">
    <svg class="paw-icon" viewBox="0 0 72 66" aria-hidden="true">
      <g fill="var(--white)">
        <ellipse cx="12" cy="28" rx="8" ry="10" transform="rotate(-20 12 28)"/>
        <ellipse cx="26" cy="12" rx="8" ry="11" transform="rotate(-8 26 12)"/>
        <ellipse cx="46" cy="12" rx="8" ry="11" transform="rotate(8 46 12)"/>
        <ellipse cx="60" cy="28" rx="8" ry="10" transform="rotate(20 60 28)"/>
        <path d="M36 32c10 0 20 12 21 22 1 8-7 11-13 9-4-1-6-2-8-2s-4 1-8 2c-6 2-14-1-13-9 1-10 11-22 21-22z"/>
      </g>
    </svg>
    <span class="address-text address-street">217 W BRANNOCK AVE</span>
    <span class="address-text address-city">TAMPA, FL 33682</span>
  </address>

  <p class="hours">OPEN: TUES-SUN<br>10AM - 7PM</p>
</main>
</body>
</html>
```